University of Carrowind Larkmoor Saxophone Quartet Concert

We need a poster design advertising the Larkmoor Saxophone Quartet Concert on Tuesday, April 23 at 5pm. The program concert will consist of 2 works by Peter Oskivar: Harbor Lanterns and Vesper ledger. These two works should be included on the poster being the concert is featuring the composer and his works. Peter Oskivar is known for his very "natural" sounding music. He resides in Montana and writes mostly from his small cottage in the mountains. This same idea of nature and "Montana" should be included on the poster design. He is deeply influenced by Telvane and most of the music he writes is play offs from Telvane Chorales.

The concert title is: "Where Quiet Rivers Meet"

Target Market(s)

Collegiate Musician, Professional Musicians, Music Faculty

Industry/Entity Type

Advertising

Requirements
Must have
• 1. Title of the Concert: "Where Quiet Rivers Meet"
2. "Larkmoor Saxophone Quartet Presents"
3. Date (April 23)
4. Time: 5pm
5. Location: Chapel of The Blessed Orrin
Nice to have
• Nice to maybe keep the idea of "Montana" and that mountian-esque feel

```html
<!DOCTYPE html>
<html lang="en">
<head>
<meta charset="utf-8">
<title>Where Quiet Rivers Meet – Larkmoor Saxophone Quartet</title>
<link rel="stylesheet" href="https://fonts.googleapis.com/css2?family=Titan+One&family=Berkshire+Swash&family=Oswald:wght@600&family=Chakra+Petch:ital,wght@1,700&display=swap">
<style>
  :root {
    --paper: #f4f4f5;
    --paper-edge: #d9d9dc;
    --red: #e21b23;
    --ink: #2a2226;
    --yellow: #fff200;
    --yellow-text: #ffe600;
    --band: #58585a;
  }
  * { margin: 0; padding: 0; box-sizing: border-box; }
  html, body { width: 1200px; height: 900px; overflow: hidden; }
  body { background: var(--paper); }

  .poster {
    position: relative;
    width: 1200px;
    height: 900px;
    overflow: hidden;
    background: radial-gradient(ellipse at 50% 45%, #ffffff 0%, var(--paper) 55%, var(--paper-edge) 100%);
  }

  .artwork {
    position: absolute;
    left: 0; top: 40px;
    width: 1200px; height: 820px;
    background:
      radial-gradient(circle at 12% 78%, rgba(226, 60, 170, .55) 0, rgba(226, 60, 170, 0) 22%),
      radial-gradient(circle at 45% 72%, rgba(255, 170, 40, .55) 0, rgba(255, 170, 40, 0) 20%),
      radial-gradient(circle at 70% 70%, rgba(230, 90, 220, .5) 0, rgba(230, 90, 220, 0) 18%),
      radial-gradient(circle at 30% 72%, rgba(60, 190, 220, .45) 0, rgba(60, 190, 220, 0) 20%),
      radial-gradient(circle at 50% 12%, rgba(255, 120, 60, .35) 0, rgba(255, 120, 60, 0) 18%),
      linear-gradient(90deg, rgba(240, 90, 90, .25), rgba(120, 200, 120, .25) 40%, rgba(90, 150, 230, .25) 70%, rgba(200, 110, 220, .25));
  }

  .band {
    position: absolute;
    left: 850px; top: 598px;
    width: 350px; height: 92px;
    background: var(--band);
  }

  .title {
    position: absolute;
    left: 0; top: 28px; width: 1200px;
    text-align: center;
    font-family: "Titan One", sans-serif;
    font-size: 56px;
    line-height: 1;
    color: var(--red);
    -webkit-text-stroke: 2px var(--ink);
    paint-order: stroke fill;
    text-shadow: 4px 4px 0 var(--ink);
  }
  .title-rule {
    position: absolute;
    left: 195px; top: 97px;
    width: 812px; height: 3px;
    background: var(--red);
  }

  .presenter {
    position: absolute;
    left: 0; top: 130px; width: 1200px;
    text-align: center;
    font-family: "Berkshire Swash", cursive;
    font-size: 54px;
    line-height: 1;
    color: var(--red);
    text-shadow: 3px 3px 0 var(--ink);
  }

  .details {
    position: absolute;
    left: 36px; top: 222px;
    font-family: "Oswald", sans-serif;
    font-weight: 600;
    font-size: 52px;
    line-height: 84px;
    color: var(--yellow-text);
    -webkit-text-stroke: 5px var(--red);
    paint-order: stroke fill;
    list-style: none;
  }

  .burst {
    position: absolute;
    left: 0; top: 0;
    width: 1200px; height: 900px;
  }
  .featuring {
    position: absolute;
    left: 640px; top: 282px; width: 400px;
    text-align: center;
    font-family: "Oswald", sans-serif;
    font-weight: 600;
    font-size: 36px;
    line-height: 1.1;
    color: var(--ink);
  }
  .featuring span { border-bottom: 3px solid var(--ink); }
  .program {
    position: absolute;
    left: 600px; top: 360px; width: 480px;
    text-align: center;
    font-family: "Chakra Petch", sans-serif;
    font-style: italic;
    font-weight: 700;
    font-size: 34px;
    line-height: 38px;
    letter-spacing: 1px;
    text-transform: uppercase;
    color: var(--ink);
  }

  .tagline {
    position: absolute;
    left: 0; top: 742px; width: 1200px;
    text-align: center;
    font-family: "Berkshire Swash", cursive;
    font-size: 62px;
    line-height: 1;
    color: var(--red);
    text-shadow: 3px 3px 0 var(--ink);
  }
</style>
</head>
<body>
  <main class="poster">
    <div class="artwork" role="img" aria-label="Colourful illustration of dancers, paint splashes, loudspeakers and equaliser bars"></div>
    <div class="band"></div>

    <h1 class="title">Where Quiet Rivers Meet</h1>
    <div class="title-rule"></div>

    <h2 class="presenter">Larkmoor Saxophone Quartet Concert Presents!!</h2>

    <ul class="details">
      <li>Date:</li>
      <li>Tuesday, April 23</li>
      <li>Time:5pm.</li>
      <li>Venue:</li>
      <li>Chapel of The Blessed Orrin</li>
    </ul>

    <svg class="burst" viewBox="0 0 1200 900" aria-hidden="true">
      <polygon fill="var(--yellow)" points="1185,385 1080,414 1159,467 1044,468 1084,537 976,510 972,584 888,532 840,600 792,532 708,584 704,510 596,537 636,468 521,467 600,414 495,385 600,356 521,303 636,302 596,233 704,260 708,186 792,238 840,170 888,238 972,186 976,260 1084,233 1044,302 1159,303 1080,356"/>
    </svg>
    <p class="featuring"><span>Featuring</span></p>
    <p class="program">Works by<br>Peter Oskivar:<br>Harbor Lanterns<br>and Vesper ledger</p>

    <p class="tagline">Montana Sounds From The Mountains</p>
  </main>
</body>
</html>
```